GLS biz card

We need a business card design for our new company based in Los Angeles called "Gold Lantern Studios". We develop film and television projects. We work with investors, financiers, film production companies, film distribution and sales companies as well as studios. We would like to incorporate our logo (see attached) on a two-sided card. We need to include: name and title, address, phone, email and company website.

Target Market(s)

Business, financial and studio clients

Industry/Entity Type

Business

Contact Information for Business Card

Two-sided. We are thinking of the logo on one side and the information on the back. Please feel free to be creative! Thanks.

Requirements
Must have
• Please include the following text information, excluding the "CAPS CATEGORY:" and please allow the ability for us to change the name, title and email address for each company employee):
• NAME & TITLE:
• Peter Dunmore
• Managing Partner
• COMPANY NAME:
• GOLD LANTERN STUDIOS (please use existing logo)
• COMPANY ADDRESS:
• KVT Arts Park
• 2480 Wexley Boulevard
• Arts Hall, 4th Floor
• Manhattan Beach, CA 90266
• COMPANY PHONE NUMBER:
• 310-555-4206
• COMPANY WEBSITE ADDRESS:
• www.goldlanternstudioshouse.com
• EMAIL ADDRESS: (only one per card)
• frank@goldlanternstudioshouse.com
• tizzy@goldlanternstudioshouse.com
• peter@goldlanternstudioshouse.com

```html
<!DOCTYPE html>
<html lang="en">
<head>
<meta charset="utf-8">
<title>Gold Lantern Studios – Business Card</title>
<link rel="stylesheet" href="https://fonts.googleapis.com/css2?family=Open+Sans:wght@400;600&display=swap">
<style>
  :root {
    --paper: #f2f2f2;
    --card-black: #040404;
    --card-edge: #151515;
    --brand-blue: #3db4e2;
    --brand-blue-deep: #17779f;
    --text-white: #f4f4f4;
    --text-soft: #cfd6da;
  }
  * { box-sizing: border-box; margin: 0; padding: 0; }
  html, body {
    width: 1200px; height: 900px; overflow: hidden;
    background: var(--paper);
    font-family: "Open Sans", sans-serif;
  }
  .stage { position: relative; width: 1200px; height: 900px; }

  .card {
    position: absolute; top: 295px;
    width: 540px; height: 310px;
    border-radius: 22px;
    background: radial-gradient(ellipse at 40% 40%, var(--card-edge) 0%, var(--card-black) 70%);
    box-shadow: 0 14px 30px rgba(0,0,0,0.22);
    overflow: hidden;
  }
  .card--front { left: 45px; }
  .card--back { left: 615px; }

  .brand-mark {
    position: absolute; border-radius: 50%;
    background: var(--brand-blue);
  }
  .card--front .brand-mark { width: 96px; height: 96px; left: 197px; top: 52px; }
  .card--back .brand-mark { width: 62px; height: 62px; left: 239px; top: 38px; }

  .brand-name {
    position: absolute; left: 0; width: 100%;
    text-align: center; color: var(--brand-blue);
    font-weight: 600; letter-spacing: 0.08em; white-space: nowrap;
  }
  .card--front .brand-name { top: 168px; font-size: 26px; left: -25px; }
  .card--back .brand-name { top: 112px; font-size: 18px; }

  .tagline {
    position: absolute; left: 0; width: 100%;
    text-align: center; color: var(--text-white);
    font-size: 8px; letter-spacing: 0.18em; font-weight: 600;
  }
  .card--front .tagline { top: 210px; left: -25px; }
  .card--back .tagline { top: 140px; font-size: 6.5px; }

  .rule {
    position: absolute; left: 0; top: 176px; width: 100%; height: 3px;
    background: linear-gradient(90deg, var(--brand-blue-deep), var(--brand-blue) 50%, var(--brand-blue-deep));
  }

  .holder {
    position: absolute; right: 352px; top: 226px; text-align: right; white-space: nowrap;
  }
  .holder-name { color: var(--brand-blue); font-size: 19px; font-weight: 400; line-height: 1.1; }
  .holder-title { color: var(--brand-blue); font-size: 10px; margin-top: 3px; }

  .divider {
    position: absolute; left: 198px; top: 208px; width: 1px; height: 84px;
    background: var(--text-soft);
  }

  .contact-list {
    position: absolute; left: 210px; top: 208px; list-style: none;
  }
  .contact-list li {
    display: flex; align-items: center; gap: 6px; white-space: nowrap;
    color: var(--text-white); font-size: 12.5px; line-height: 20px;
  }
  .contact-list svg { width: 12px; height: 12px; fill: var(--text-white); flex: none; }
</style>
</head>
<body>
<main class="stage">

  <section class="card card--front" aria-label="Card front">
    <span class="brand-mark"></span>
    <p class="brand-name">GOLD LANTERN STUDIOS</p>
    <p class="tagline">A MEDIA ENTERTAINMENT COMPANY</p>
  </section>

  <section class="card card--back" aria-label="Card back">
    <span class="brand-mark"></span>
    <p class="brand-name">GOLD LANTERN STUDIOS</p>
    <p class="tagline">A MEDIA ENTERTAINMENT COMPANY</p>
    <span class="rule"></span>

    <div class="holder">
      <p class="holder-name">Peter Dunmore</p>
      <p class="holder-title">Managing Partner</p>
    </div>
    <span class="divider"></span>

    <ul class="contact-list">
      <li>
        <svg viewBox="0 0 24 24"><path d="M6.6 10.8a15.1 15.1 0 0 0 6.6 6.6l2.2-2.2a1 1 0 0 1 1-.25 11.4 11.4 0 0 0 3.6.57 1 1 0 0 1 1 1V20a1 1 0 0 1-1 1A17 17 0 0 1 3 4a1 1 0 0 1 1-1h3.5a1 1 0 0 1 1 1c0 1.25.2 2.45.57 3.57a1 1 0 0 1-.25 1z"/></svg>
        310-555-4206
      </li>
      <li>
        <svg viewBox="0 0 24 24"><path d="M12 2a10 10 0 1 0 0 20 10 10 0 0 0 0-20zm6.9 6h-3a15.7 15.7 0 0 0-1.4-3.6A8 8 0 0 1 18.9 8zM12 4a14 14 0 0 1 1.9 4h-3.8A14 14 0 0 1 12 4zM4.3 14a8 8 0 0 1 0-4h3.4a16.5 16.5 0 0 0 0 4zm.8 2h3a15.7 15.7 0 0 0 1.4 3.6A8 8 0 0 1 5.1 16zm3-8h-3a8 8 0 0 1 4.4-3.6A15.7 15.7 0 0 0 8.1 8zM12 20a14 14 0 0 1-1.9-4h3.8A14 14 0 0 1 12 20zm2.3-6H9.7a14.7 14.7 0 0 1 0-4h4.6a14.7 14.7 0 0 1 0 4zm.2 5.6a15.7 15.7 0 0 0 1.4-3.6h3a8 8 0 0 1-4.4 3.6zm1.8-5.6a16.5 16.5 0 0 0 0-4h3.4a8 8 0 0 1 0 4z"/></svg>
        www.goldlanternstudioshouse.com
      </li>
      <li>
        <svg viewBox="0 0 24 24"><path d="M2 5h20v14H2zm2 2v.4l8 5.2 8-5.2V7zm0 2.8V17h16V9.8l-8 5.2z"/></svg>
        peter@goldlanternstudioshouse.com
      </li>
      <li>
        <svg viewBox="0 0 24 24"><path d="M12 3 2 12h3v8h5v-6h4v6h5v-8h3z"/></svg>
        2480 Wexley Blvd. Manhattan Beach, CA 90266
      </li>
    </ul>
  </section>

</main>
</body>
</html>
```